Rising Paths Web Design

I am starting a new company that will provide LIFE COACHING services - I have tried to design a website, but it's too complicated. Right now, it's just me - I'm the only person that will provide services through the website - I have used artmarket to purchase a logo (see below). I want to be able to update the website myself, but need a template - basic design. Because I am not technologically savvy enough to explain in words - I basically want to have a website that will provide basic information about my services (coaching), a page about me and my background, hopefully scheduling possibilities, and testimonials — also a page for writing/blogs. I bought a website through NetHarbor - so when I have a template, I guess I”d use that - but maybe I’ll need to work with a designer to actually get it up on the internet. I have a head shot that I’ll upload, too.
Target Market(s)
Clients from the independent (private school) world - teachers, administrators
Number of Pages Required
4 page
Look and feel
Each slider illustrates characteristics of the customer's brand and the style your logo design should communicate.

```html
<!DOCTYPE html>
<html lang="en">
<head>
<meta charset="utf-8">
<title>Rising Paths – Web Design</title>
<link href="https://fonts.googleapis.com/css2?family=Lora:wght@400;500&family=Montserrat:wght@400;500&family=Arimo:wght@400&display=swap" rel="stylesheet">
<style>
  :root{
    --teal:#08ae92;
    --teal-deep:#03ab8f;
    --teal-soft:#66d8c8;
    --teal-bright:#00bba3;
    --mint:#e8f7f4;
    --white:#ffffff;
    --grey:#808080;
    --ink:#222222;
    --text:#3a3a3a;
  }
  *{margin:0;padding:0;box-sizing:border-box}
  html,body{width:1200px;height:1200px;overflow:hidden;background:var(--white)}
  .canvas{position:relative;width:1200px;height:1200px;background:var(--white)}
  .abs{position:absolute}
  .serif{font-family:'Lora',Georgia,serif}
  .sans{font-family:'Montserrat',Arial,sans-serif}

  /* website mock */
  .topbar{left:115px;top:0;width:426px;height:10px;background:var(--teal)}
  .social{top:2.5px;width:5px;height:5px;border:0.8px solid var(--white);border-radius:1px}
  .header{left:115px;top:10px;width:426px;height:39px;background:var(--mint)}
  .brand-dot{left:150px;top:16px;width:28px;height:28px;border-radius:50%;border:0.8px solid var(--teal)}
  .brand-name{left:152px;top:27px;width:24px;font-size:3.6px;color:var(--teal);text-align:center;letter-spacing:.1px;line-height:1.1}
  .nav{top:28px;font-size:5.3px;color:var(--text)}

  .hero{left:115px;top:49px;width:426px;height:270px;
    background:linear-gradient(90deg,#c2a99a 0%,#b3b1a4 22%,#8fc3b4 42%,#4fcab0 62%,var(--teal) 85%)}
  .hero-small{font-size:12px;color:var(--white)}
  .hero-big{font-size:23px;line-height:20px;color:var(--white);font-weight:500}

  .about{left:115px;top:319px;width:426px;height:252px;background:var(--mint)}
  .badge{top:389px;height:25px}
  .quote{font-size:12.5px;line-height:12.5px;color:var(--text)}
  .more{font-size:5px;color:var(--teal)}
  .portrait{left:368px;top:347px;width:143px;height:191px;
    background:linear-gradient(160deg,#c9c2b5 0%,#e2d6c6 45%,#bfb4a8 100%)}

  .card{top:604px;width:110px;height:109px;color:var(--white)}
  .card-title{position:absolute;left:7px;top:43px;font-size:12.5px;line-height:12.5px}
  .card-more{position:absolute;right:10px;bottom:6px;font-size:4.6px}
  .card svg{position:absolute;left:5px;top:15px}

  .testimonials{left:115px;top:743px;width:426px;height:196px;background:var(--mint)}
  .avatar{left:242px;top:786px;width:34px;height:33px;background:linear-gradient(160deg,#b9c3b6,#5d6d5d)}
  .client{left:279px;top:797px;font-size:5px;line-height:5px;color:var(--grey)}

  .contact{left:115px;top:939px;width:426px;height:252px;
    background:linear-gradient(90deg,#b9bfd2 0%,#a9c5d4 25%,#8fd2c4 45%,#3dc2a6 65%,var(--teal) 85%)}
  .field{left:400px;width:94px;border:0.7px solid rgba(255,255,255,.85);font-size:4.6px;color:var(--white);padding:3px 5px}
  .footer{left:115px;top:1192px;width:426px;text-align:center;font-size:4.6px;color:var(--teal)}

  /* guide */
  .guide-title{font-family:'Arimo',Arial,sans-serif;color:var(--ink);font-size:30px;letter-spacing:-.5px}
  .swatch{top:456px;width:82px;height:82px;border-radius:50%;box-shadow:3px 6px 10px rgba(0,0,0,.18)}
  .font-line{color:var(--ink);white-space:nowrap}
</style>
</head>
<body>
<div class="canvas">

  <!-- header -->
  <div class="abs topbar"></div>
  <div class="abs social" style="left:489px"></div>
  <div class="abs social" style="left:497px"></div>
  <div class="abs social" style="left:505px"></div>
  <div class="abs header"></div>
  <div class="abs brand-dot"></div>
  <div class="abs brand-name serif">RISING PATHS</div>
  <div class="abs nav serif" style="left:347px">About Me</div>
  <div class="abs nav serif" style="left:377px">Services</div>
  <div class="abs nav serif" style="left:405px">Testimonials</div>
  <div class="abs nav serif" style="left:443px">Schedule A Meeting</div>
  <div class="abs nav serif" style="left:499px">Blog</div>

  <!-- hero -->
  <div class="abs hero" role="img" aria-label="Photo of a woman working on a laptop by a bright window, fading into teal"></div>
  <div class="abs hero-small serif" style="left:360px;top:128px">Way to a</div>
  <div class="abs hero-big sans" style="left:359px;top:145px">Better &amp;<br>Growing Life</div>
  <div class="abs hero-small serif" style="left:362px;top:186px">starts now</div>

  <!-- about -->
  <div class="abs about"></div>
  <div class="abs badge" style="left:144px;width:25px;border-radius:50%;border:2px solid #2a9ad6;background:var(--white)"></div>
  <div class="abs badge" style="left:175px;width:22px;background:#2d5a86;border-top:6px solid #f2f2f2"></div>
  <div class="abs badge" style="left:207px;width:22px;background:#1f5b8c;border-radius:2px"></div>
  <div class="abs quote serif" style="left:143px;top:425px;width:200px">“In vel orci aliquet, semper tellus nec, lacinia sem. Aenean &nbsp;justo, luctus vel dignissim a, vulputate nec eros. Maecenas tempor finibus erat at euismod.”</div>
  <div class="abs more sans" style="left:143px;top:495px">Read More About Me</div>
  <svg class="abs" style="left:325px;top:450px" width="90" height="95" viewBox="0 0 90 95">
    <circle cx="47" cy="47" r="40.5" fill="none" stroke="#08ae92" stroke-width="0.8"/>
  </svg>
  <div class="abs portrait" role="img" aria-label="Headshot of the coach in a kitchen"></div>

  <!-- services -->
  <div class="abs card" style="left:164px;background:var(--teal-deep)">
    <svg width="20" height="18" viewBox="0 0 20 18" fill="none" stroke="#fff" stroke-width="0.9">
      <rect x="1" y="2" width="3" height="14"/><rect x="4.5" y="2" width="3" height="14"/><rect x="8" y="2" width="3" height="14"/>
      <path d="M12 3 L15 2.4 L18 15 L15 15.6 Z"/><line x1="0" y1="16.5" x2="20" y2="16.5"/>
    </svg>
    <div class="card-title serif">Help<br>With<br>The Books</div>
    <div class="card-more sans">Know More</div>
  </div>
  <div class="abs card" style="left:274px;background:var(--teal-soft)">
    <svg width="18" height="18" viewBox="0 0 18 18" fill="none" stroke="#fff" stroke-width="0.9">
      <circle cx="9" cy="9" r="7.5"/><path d="M12 6 L10 10 L6 12 L8 8 Z"/>
    </svg>
    <div class="card-title serif">Help<br>With<br>Direction</div>
    <div class="card-more sans">Know More</div>
  </div>
  <div class="abs card" style="left:383px;background:var(--teal-bright)">
    <svg width="20" height="20" viewBox="0 0 20 20" fill="none" stroke="#fff" stroke-width="0.9">
      <path d="M7 1 q-1.5 1.5 0 3 M10 1 q-1.5 1.5 0 3"/>
      <path d="M2 6 H14 V13 Q14 18 8 18 Q2 18 2 13 Z"/><path d="M14 8 H17 V12 H14"/>
      <rect x="4" y="9" width="3" height="3"/>
    </svg>
    <div class="card-title serif">Help<br>With<br>Physical Health</div>
    <div class="card-more sans">Know More</div>
  </div>

  <!-- testimonials -->
  <div class="abs testimonials"></div>
  <div class="abs avatar" role="img" aria-label="Client portrait photo"></div>
  <div class="abs client sans">Sarah Doe<br>2018-2019</div>
  <div class="abs quote serif" style="left:242px;top:828px;width:190px">“In vel orci aliquet, semper tellus nec, lacinia sem. Aenean &nbsp;justo, luctus vel dignissim a, vulputate nec eros.</div>
  <div class="abs more sans" style="left:242px;top:888px">Read More Testimonials</div>
  <svg class="abs" style="left:204px;top:834px" width="14" height="14" viewBox="0 0 14 14" fill="none" stroke="#08ae92" stroke-width="0.8">
    <circle cx="7" cy="7" r="6"/><path d="M8 5 L6 7 L8 9"/>
  </svg>
  <svg class="abs" style="left:439px;top:834px" width="14" height="14" viewBox="0 0 14 14" fill="none" stroke="#08ae92" stroke-width="0.8">
    <circle cx="7" cy="7" r="6"/><path d="M6 5 L8 7 L6 9"/>
  </svg>

  <!-- contact -->
  <div class="abs contact" role="img" aria-label="Photo of a smiling woman in a coaching session, fading into teal"></div>
  <div class="abs serif" style="left:399px;top:980px;font-size:12.5px;line-height:12.5px;color:var(--white)">Get in touch with<br>the best</div>
  <div class="abs field sans" style="top:1017px;height:15px">Full Name</div>
  <div class="abs field sans" style="top:1041px;height:15px">Email</div>
  <div class="abs field sans" style="top:1067px;height:43px">Explain What You Need Help With</div>
  <div class="abs sans" style="left:400px;top:1118px;width:94px;text-align:center;font-size:4.8px;color:var(--white)">SUBMIT</div>
  <div class="abs footer sans">All Rights Reserved 2022</div>

  <!-- style guide -->
  <div class="abs guide-title" style="left:615px;top:406px">COLOR PALETTE</div>
  <div class="abs swatch" style="left:615px;background:var(--teal)"></div>
  <div class="abs swatch" style="left:718px;background:var(--white)"></div>
  <div class="abs swatch" style="left:821px;background:var(--mint)"></div>
  <div class="abs swatch" style="left:923px;background:var(--grey)"></div>

  <div class="abs guide-title" style="left:619px;top:664px">FONT FAMILY</div>
  <div class="abs font-line sans" style="left:615px;top:707px;font-size:40px">Montserrat for links/buttons</div>
  <div class="abs font-line serif" style="left:612px;top:762px;font-size:44px">Lora for headings &amp; text</div>

</div>
</body>
</html>
```